Design a Static Leaderboard Banner for Dog Walking Business

I require one 729x90 Leaderboard.
Please see attached logo and screenshot of website.

- Colours used should be in line with the website
- Text to be included: "Dog Walking & Holiday Services on Sydney's North"
- Promotional Text to be included: "$25 off your 1st Spend*", with very small font in bottom right corner stating "*Min. Spend $50"
- Phone number to be included: "0417 265 093"
- If space permits also add: "Lowest Price Guarantee"

This banner should use subtle colours and have clean lines.
Please ask if you have any questions.

```html
<!DOCTYPE html>
<html lang="en">
<head>
<meta charset="utf-8">
<title>Leash Lane – Leaderboard Banner</title>
<link rel="stylesheet" href="https://fonts.googleapis.com/css2?family=Nunito:wght@800&family=Cabin:wght@400;500&family=Arimo:wght@400&display=swap">
<style>
  :root {
    --brand-blue: #2f6fbf;
    --band-blue-top: #2d86d8;
    --band-blue-bottom: #1a5fb4;
    --mid-blue-top: #2eaaea;
    --mid-blue-bottom: #1c7ad2;
    --panel-top: #ffffff;
    --panel-bottom: #dfe3e8;
    --promo-orange: #f7a21b;
    --promo-orange-deep: #f28c12;
    --ribbon-green: #3e9a2f;
    --page-dark: #3f3f3f;
    --page-mid: #5f5f5f;
    --slide-white: #ffffff;
    --caption-orange: #ec5a1c;
    --white: #ffffff;
  }
  * { margin: 0; padding: 0; box-sizing: border-box; }
  html, body { width: 1200px; height: 629px; overflow: hidden; }
  body {
    position: relative;
    background: linear-gradient(180deg, var(--page-mid), var(--page-dark) 70%, #4b4b4b);
    font-family: "Cabin", sans-serif;
  }

  /* ---------- Leaderboard ---------- */
  .leaderboard {
    position: absolute; left: 0; top: 0; width: 1200px; height: 148px;
    background: linear-gradient(180deg, var(--band-blue-top), var(--band-blue-bottom));
  }
  .brand-panel {
    position: absolute; left: 0; top: 0; width: 486px; height: 148px;
    background: linear-gradient(180deg, var(--panel-top), var(--panel-bottom));
    border-radius: 0 0 22px 0;
    display: flex; align-items: center; gap: 16px; padding-left: 26px;
  }
  .brand-dot {
    width: 52px; height: 52px; border-radius: 50%;
    background: var(--brand-blue);
  }
  .brand-name {
    font-family: "Nunito", sans-serif; font-weight: 800;
    font-size: 44px; color: var(--brand-blue); letter-spacing: -0.5px;
  }
  .service-panel {
    position: absolute; left: 486px; top: 0; width: 378px; height: 148px;
    background: linear-gradient(180deg, var(--mid-blue-top), var(--mid-blue-bottom));
    color: var(--white); text-align: center;
  }
  .service-line {
    font-size: 26px; line-height: 1; position: absolute; left: 0; width: 100%;
  }
  .service-line.first { top: 15px; }
  .service-line.second { top: 55px; }
  .service-phone {
    position: absolute; left: 0; width: 100%; top: 96px;
    display: flex; justify-content: center; align-items: center; gap: 12px;
    font-size: 36px; line-height: 1;
  }
  .service-phone svg { width: 38px; height: 38px; }
  .promo-panel {
    position: absolute; left: 864px; top: 0; width: 300px; height: 148px;
    background: linear-gradient(180deg, var(--promo-orange), var(--promo-orange-deep));
    border-radius: 0 0 22px 22px;
    color: var(--white);
  }
  .promo-amount {
    position: absolute; left: 18px; top: 2px; font-size: 56px; line-height: 1; font-weight: 500;
  }
  .promo-text {
    position: absolute; left: 18px; font-size: 29px; line-height: 1;
  }
  .promo-text.off { top: 62px; }
  .promo-text.spend { top: 94px; }
  .promo-text sup { font-size: 16px; }
  .promo-note {
    position: absolute; left: 22px; top: 126px; font-size: 14px;
  }
  .price-badge {
    position: absolute; left: 1048px; top: 8px; width: 140px; height: 120px;
  }

  /* ---------- Website hero ---------- */
  .hero-slide {
    position: absolute; left: 46px; top: 171px; width: 909px; height: 333px;
    background: var(--slide-white);
    box-shadow: 0 4px 10px rgba(0,0,0,0.35);
  }
  .slide-brand {
    position: absolute; left: 523px; top: 26px;
    display: flex; align-items: center; gap: 12px;
  }
  .slide-brand .brand-dot { width: 50px; height: 50px; background: #2a9fe0; }
  .slide-brand .brand-name { font-family: "Arimo", sans-serif; font-weight: 400; font-size: 40px; color: #2a9fe0; }
  .pet-lineup {
    position: absolute; left: 61px; top: 132px; width: 774px; height: 192px;
    background: linear-gradient(90deg, #b8a79a, #d9d2c8 30%, #c89a6a 50%, #cfc7bd 75%, #b9b2aa);
    border-radius: 8px;
    opacity: 0.85;
  }
  .slider-controls {
    position: absolute; left: 448px; top: 526px; width: 104px; height: 20px;
  }
  .hero-caption {
    position: absolute; left: 46px; top: 562px; font-family: "Arimo", sans-serif;
  }
  .caption-title { color: var(--white); font-size: 25px; line-height: 1.1; }
  .caption-sub { color: var(--caption-orange); font-size: 14px; margin-top: 6px; }
</style>
</head>
<body>
  <header class="leaderboard">
    <div class="brand-panel">
      <span class="brand-dot"></span>
      <span class="brand-name">Leash Lane</span>
    </div>

    <div class="service-panel">
      <p class="service-line first">Dog Walking &amp; Holiday Services</p>
      <p class="service-line second">on Sydney's North</p>
      <p class="service-phone">
        <svg viewBox="0 0 40 40" aria-hidden="true">
          <circle cx="20" cy="20" r="17" fill="none" stroke="#fff" stroke-width="3"/>
          <path d="M14 11c1.5-1 2.5-.5 3.3 1l1.4 2.8c.6 1.2.2 2-.8 2.7l-1 .7c.9 2.4 2.6 4.3 4.9 5.4l.8-1c.8-1 1.6-1.3 2.8-.6l2.7 1.6c1.4.9 1.7 1.9.6 3.3-1.3 1.7-3.2 2.3-5.3 1.4-5.5-2.2-9.4-6.3-11-11.9-.6-2.1.2-4 1.6-5.4z" fill="#fff"/>
        </svg>
        0417 265 093
      </p>
    </div>

    <div class="promo-panel">
      <p class="promo-amount">$25</p>
      <p class="promo-text off">off your</p>
      <p class="promo-text spend">1<sup>st</sup> Spend*</p>
      <p class="promo-note">*Min. Spend $50</p>
    </div>

    <svg class="price-badge" viewBox="0 0 140 120" aria-label="Lowest Price Guarantee">
      <g transform="rotate(-18 70 60)">
        <circle cx="70" cy="56" r="50" fill="#1e8fd6" stroke="#ffffff" stroke-width="4"/>
        <text x="70" y="44" text-anchor="middle" fill="#fff" font-family="Arimo, sans-serif" font-size="20" font-weight="700">LOWEST</text>
        <text x="70" y="66" text-anchor="middle" fill="#fff" font-family="Arimo, sans-serif" font-size="20" font-weight="700">PRICE</text>
        <path d="M6 72 H134 L126 82 L134 92 H6 L14 82 Z" fill="var(--ribbon-green)"/>
        <text x="70" y="87" text-anchor="middle" fill="#fff" font-family="Arimo, sans-serif" font-size="12" font-weight="700">GUARANTEE</text>
      </g>
    </svg>
  </header>

  <section class="hero-slide">
    <div class="slide-brand">
      <span class="brand-dot"></span>
      <span class="brand-name">Leash Lane</span>
    </div>
    <div class="pet-lineup" role="img" aria-label="Row of pets sitting side by side: ferret, cats, dalmatian, parrot with fishbowl, collie, rabbit, guinea pig and mouse"></div>
  </section>

  <svg class="slider-controls" viewBox="0 0 104 20" aria-hidden="true">
    <circle cx="10" cy="10" r="9" fill="#2b2b2b"/>
    <path d="M12 5 L7 10 L12 15" fill="none" stroke="#fff" stroke-width="2.2"/>
    <circle cx="38" cy="10" r="4" fill="#777"/>
    <circle cx="52" cy="10" r="6" fill="#e6e6e6"/>
    <circle cx="66" cy="10" r="4" fill="#777"/>
    <circle cx="94" cy="10" r="9" fill="#2b2b2b"/>
    <path d="M92 5 L97 10 L92 15" fill="none" stroke="#fff" stroke-width="2.2"/>
  </svg>

  <div class="hero-caption">
    <p class="caption-title">Leash Lane</p>
    <p class="caption-sub">Dog and Cat Sitting - Pet Minding Services, Mosman Sydney</p>
  </div>
</body>
</html>
```